FLYER: Human Factors in Traffic Crashes - Analysis of Drivers' Responses - training

We are hosting a class in Australia 30, November to 4, December 2020. I would like to have a flyer designed to "sell" the class with description of course topics. I have uploaded a flyer I started on my own but I want it to be professional. Dr. Pelloway only gets to AU every 3-5 years to teach from the US. I would like to have some type of roadway scenery, prefer a nighttime scene.

Target Market(s)

Accident reconstructionists and engineers, police reconstructionists.

Font styles to use
Serif

Colors
fec214

Requirements
Must have
• Name of course and course topics, location of course, price, website and contact information.
Nice to have
• Some type of roadway background, possibly a nighttime scene on a roadway.

```html
<!DOCTYPE html>
<html lang="en">
<head>
<meta charset="utf-8">
<title>Human Factors in Traffic Crashes – Course Flyer</title>
<link href="https://fonts.googleapis.com/css2?family=Oswald:wght@300;500;600&family=Lato:ital,wght@0,400;0,700;1,400&family=Roboto+Slab:wght@600;700&display=swap" rel="stylesheet">
<style>
  :root{
    --yellow:#fbbd35;
    --charcoal:#3a3a3c;
    --ink:#2f2f31;
    --paper:#f4f4f4;
    --backdrop:#ececec;
    --white:#ffffff;
    --rule:#5a5a5c;
    --night-dark:#262628;
    --night-mid:#3b3b3d;
    --night-glow:#5b5b5d;
  }
  *{box-sizing:border-box;margin:0;padding:0}
  html,body{width:928px;height:1200px;overflow:hidden;background:var(--backdrop)}
  .flyer{position:absolute;left:62px;top:30px;width:805px;height:1140px;background:var(--paper);overflow:hidden;font-family:"Lato",sans-serif;color:var(--ink)}
  .masthead{position:absolute;left:0;top:0;width:805px;height:131px;background:var(--white)}
  .brand{position:absolute;left:49px;top:30px;display:flex;align-items:center;gap:12px}
  .brand-mark{width:46px;height:46px;background:var(--yellow)}
  .brand-name{font-family:"Oswald",sans-serif;font-weight:600;font-size:30px;line-height:1.05;color:var(--ink);letter-spacing:.5px}
  .hero{position:absolute;left:0;top:131px;width:805px;height:392px}
  .hero-bg{position:absolute;inset:0;
    background:
      radial-gradient(ellipse 230px 300px at 360px 420px, rgba(120,120,122,.55) 0%, rgba(90,90,92,.25) 45%, rgba(0,0,0,0) 75%),
      radial-gradient(ellipse 160px 60px at 330px 90px, rgba(150,150,152,.35) 0%, rgba(0,0,0,0) 70%),
      linear-gradient(180deg,var(--night-dark) 0%,var(--night-mid) 55%,#434345 100%)}
  .hero-band{position:absolute;left:0;top:523px;width:805px;height:22px;background:var(--yellow)}
  .hero-art{position:absolute;left:0;top:0;width:805px;height:600px}
  .title{position:absolute;left:36px;font-family:"Oswald",sans-serif;font-size:44px;line-height:1;letter-spacing:-.5px;white-space:nowrap;transform:scaleX(.83);transform-origin:left top}
  .title-lead{top:234px;color:var(--yellow);font-weight:300}
  .title-main{color:var(--white);font-weight:600}
  .title-main.l1{top:288px}
  .title-main.l2{top:342px}
  .presenter{position:absolute;left:37px;top:424px;font-size:22px;font-weight:700;color:var(--white);line-height:35px;white-space:nowrap}
  .presenter .name{color:var(--yellow)}
  .tab{position:absolute;background:var(--charcoal);color:var(--white);font-family:"Roboto Slab",serif;font-weight:700;font-size:26px;display:flex;align-items:center;justify-content:center}
  .tab-fee{left:41px;top:569px;width:314px;height:38px;clip-path:polygon(6% 0,100% 0,94% 100%,0 100%)}
  .tab-location{left:41px;top:824px;width:314px;height:38px;clip-path:polygon(6% 0,100% 0,94% 100%,0 100%)}
  .tab-rule{position:absolute;left:162px;width:177px;height:2px;background:var(--yellow)}
  .price{position:absolute;left:41px;top:640px;font-family:"Roboto Slab",serif;font-weight:600;font-size:28px;white-space:nowrap}
  .price .sep{color:var(--yellow);margin:0 10px;font-weight:400}
  .divider{position:absolute;left:23px;width:336px;height:1px;background:var(--rule)}
  .divider::before{content:"";position:absolute;left:0;top:-2px;width:60px;height:4px;background:var(--yellow)}
  .note{position:absolute;left:24px;top:720px;width:340px;font-size:15.4px;line-height:23px;font-weight:700;color:#3c3c3e}
  .address{position:absolute;left:24px;top:882px;font-size:15.4px;line-height:23px;font-weight:700;color:#3c3c3e;white-space:nowrap}
  .register-rule{position:absolute;left:0;top:994px;width:188px;height:2px;background:var(--yellow)}
  .register{position:absolute;left:0;top:997px;width:224px;height:39px;background:var(--charcoal);clip-path:polygon(0 0,82% 0,100% 100%,0 100%);color:var(--white);font-family:"Roboto Slab",serif;font-weight:700;font-size:26px;padding-left:36px;line-height:39px}
  .topics-head{position:absolute;left:393px;top:566px;font-family:"Roboto Slab",serif;font-weight:700;font-size:31px;letter-spacing:.3px;color:var(--ink);white-space:nowrap}
  .topics-rule{position:absolute;left:393px;top:607px;width:270px;height:1px;background:var(--rule)}
  .topics-rule::before{content:"";position:absolute;left:0;top:-1px;width:48px;height:4px;background:var(--yellow)}
  .topics{list-style:none}
  .topics li{position:absolute;left:393px;width:412px;padding-left:34px;font-style:italic;font-size:13.6px;line-height:20px;color:#333;white-space:nowrap}
  .topics li svg{position:absolute;left:0;top:5px}
  .footer-rule{position:absolute;left:0;top:1046px;width:805px;height:4px;background:var(--yellow)}
  .footer{position:absolute;left:0;top:1051px;width:805px;height:89px;background:var(--charcoal);color:var(--white)}
  .footer-label{position:absolute;top:26px;font-family:"Oswald",sans-serif;font-weight:500;font-size:19px;letter-spacing:.5px}
  .footer-label::after{content:"";position:absolute;left:0;top:31px;width:100%;height:1px;background:#8a8a8c}
  .footer-label::before{content:"";position:absolute;left:0;top:30px;width:36%;height:3px;background:var(--yellow)}
  .label-web{left:24px;width:104px}
  .label-contact{left:406px;width:113px}
  .web-lines{position:absolute;left:147px;top:14px;font-size:14.6px;line-height:28px}
  .footer-split{position:absolute;left:395px;top:21px;width:1px;height:63px;background:#cfcfcf}
  .phone{position:absolute;left:540px;top:26px;font-size:28px;font-weight:700;letter-spacing:.5px}
</style>
</head>
<body>
<main class="flyer">
  <header class="masthead">
    <div class="brand">
      <span class="brand-mark"></span>
      <span class="brand-name">ROADWISE<br>SAFETY INSTITUTE</span>
    </div>
  </header>

  <section class="hero">
    <div class="hero-bg" role="img" aria-label="Nighttime roadway with street lights stretching into the distance"></div>
  </section>
  <div class="hero-band"></div>

  <svg class="hero-art" viewBox="0 0 805 600">
    <defs>
      <linearGradient id="harbour" x1="0" y1="0" x2="0" y2="1">
        <stop offset="0" stop-color="#c9cdd0"/>
        <stop offset=".45" stop-color="#9aa5a8"/>
        <stop offset=".65" stop-color="#5f7d4f"/>
        <stop offset="1" stop-color="#2f5a63"/>
      </linearGradient>
    </defs>
    <polygon points="609,0 805,0 805,511 767,569 414,203" fill="var(--yellow)"/>
    <polygon points="632,0 805,0 805,508 767,546 437,203" fill="url(#harbour)" role="img" aria-label="Aerial view of a waterfront city skyline with parkland and a ferry pier"/>
  </svg>

  <h1>
    <span class="title title-lead">HUMAN FACTORS</span>
    <span class="title title-main l1">IN TRAFFIC CRASHES -</span>
    <span class="title title-main l2">ANALYSIS OF DRIVERS' RESPONSES</span>
  </h1>
  <p class="presenter">Presented by: <span class="name">Daniel Pelloway Ph.D.</span><br>World renowned Human Factors expert</p>

  <div class="tab tab-fee">Course Fee :</div>
  <div class="tab-rule" style="top:611px"></div>
  <p class="price">$1,730 AU<span class="sep">|</span>$1,200 USD</p>
  <div class="divider" style="top:698px"></div>
  <p class="note">It has been 3 years since Dr. Pelloway has come to AU to teach, don’t miss out on this year’s class.</p>

  <div class="tab tab-location">Location:</div>
  <div class="tab-rule" style="top:866px"></div>
  <p class="address">Harbourview Lodge – Coastal Headland Park<br>12 Bluff Point Road, Seacliff NSW</p>
  <div class="divider" style="top:963px"></div>

  <div class="register-rule"></div>
  <div class="register">Register</div>

  <h2 class="topics-head">COURSE TOPICS</h2>
  <div class="topics-rule"></div>
  <ul class="topics">
    <li style="top:624px"><svg width="12" height="12" viewBox="0 0 12 12"><polyline points="3,1 9,6 3,11" fill="none" stroke="var(--yellow)" stroke-width="3"/></svg>Perception-Response Time</li>
    <li style="top:653px"><svg width="12" height="12" viewBox="0 0 12 12"><polyline points="3,1 9,6 3,11" fill="none" stroke="var(--yellow)" stroke-width="3"/></svg>Response to slow moving or stopped vehicles on multilane<br>high speed roads</li>
    <li style="top:704px"><svg width="12" height="12" viewBox="0 0 12 12"><polyline points="3,1 9,6 3,11" fill="none" stroke="var(--yellow)" stroke-width="3"/></svg>Nighttime recognition</li>
    <li style="top:737px"><svg width="12" height="12" viewBox="0 0 12 12"><polyline points="3,1 9,6 3,11" fill="none" stroke="var(--yellow)" stroke-width="3"/></svg>Headlight mapping demonstration and instruction</li>
    <li style="top:769px"><svg width="12" height="12" viewBox="0 0 12 12"><polyline points="3,1 9,6 3,11" fill="none" stroke="var(--yellow)" stroke-width="3"/></svg>Driver decision making Research in IDRR</li>
    <li style="top:802px"><svg width="12" height="12" viewBox="0 0 12 12"><polyline points="3,1 9,6 3,11" fill="none" stroke="var(--yellow)" stroke-width="3"/></svg>Gap acceptance for left turns, right turns, and through<br>movements for drivers, riders, and pedestrians</li>
    <li style="top:848px"><svg width="12" height="12" viewBox="0 0 12 12"><polyline points="3,1 9,6 3,11" fill="none" stroke="var(--yellow)" stroke-width="3"/></svg>Pedestrian walking speeds Acceleration</li>
    <li style="top:882px"><svg width="12" height="12" viewBox="0 0 12 12"><polyline points="3,1 9,6 3,11" fill="none" stroke="var(--yellow)" stroke-width="3"/></svg>Lateral acceleration (swerving) for cars, motorcycles, and<br>commercial vehicles</li>
    <li style="top:926px"><svg width="12" height="12" viewBox="0 0 12 12"><polyline points="3,1 9,6 3,11" fill="none" stroke="var(--yellow)" stroke-width="3"/></svg>Forward and backward acceleration of cars, motorcycles<br>and commercial vehicles</li>
    <li style="top:972px"><svg width="12" height="12" viewBox="0 0 12 12"><polyline points="3,1 9,6 3,11" fill="none" stroke="var(--yellow)" stroke-width="3"/></svg>Drivers’ responses to green and yellow traffic signals,<br>deceleration choice, reaction time and probability of stopping</li>
  </ul>

  <div class="footer-rule"></div>
  <footer class="footer">
    <span class="footer-label label-web">WEBSITE :</span>
    <p class="web-lines">www.roadwisesafety.com<br>info@roadwisesafety.com</p>
    <span class="footer-split"></span>
    <span class="footer-label label-contact">CONTACT :</span>
    <p class="phone">555-014-2290</p>
  </footer>
</main>
</body>
</html>
```